Bright Harbor Business Cards & Stationary
Bright Harbor
Bright Harbor Business Cards & Stationary -
Creative Brief
Professional
Dana Verick
4417 Wexmoor Lane Bozeman, MT 59263
dana@brightharborfunds.example
www.brightharborfunds.example
I have two companies, Bright Harbor Wealth Management, LLC and Bright Harbor Realty Advisors, LLC. I use the same logo for both companies with a different tagline and color for each company. I will use one business card for both companies with one company on one side of the card and the other company on the other side of the card. Other than the colors, the business cards and stationary will have the same design.
Bright Harbor Realty Advisors logo Dana Verick 4417 Wexmoor Lane Bozeman, MT 59263 406-739-4802 dana@brightharborestates.example www.brightharborestates.example

```html
<!DOCTYPE html>
<html lang="en">
<head>
<meta charset="utf-8">
<title>Bright Harbor Business Cards &amp; Stationary</title>
<link rel="stylesheet" href="https://fonts.googleapis.com/css2?family=Cinzel:wght@700&family=Open+Sans:wght@400;600&display=swap">
<style>
  :root{
    --backdrop:#7b5b40;
    --paper:#ffffff;
    --paper-edge:#d9d4cc;
    --navy:#1d3557;
    --wealth-blue:#2f7db8;
    --realty-brown:#6b4a2e;
    --ink:#4a4a4a;
    --label:#e9dccd;
  }
  *{margin:0;padding:0;box-sizing:border-box}
  html,body{width:1200px;height:346px;overflow:hidden;background:var(--backdrop)}
  .canvas{position:relative;width:1200px;height:346px;font-family:"Open Sans",Arial,sans-serif;color:var(--ink)}
  .piece{position:absolute;background:var(--paper);box-shadow:0 2px 6px rgba(0,0,0,.35)}
  .brand{display:flex;align-items:center;gap:4px;font-family:"Cinzel",Georgia,serif;font-weight:700;color:var(--navy);line-height:1;white-space:nowrap}
  .brand-square{display:inline-block;flex:none;background:var(--navy)}
  .label{position:absolute;font-size:7px;color:var(--label);text-align:center;line-height:1.2}

  .showcase-brand{position:absolute;left:22px;top:76px;width:130px}
  .showcase-brand .brand{font-size:11px;color:var(--paper)}
  .showcase-brand .brand-square{width:10px;height:10px;background:var(--paper)}
  .showcase-sub{font-size:6.5px;color:var(--label);margin-top:7px;padding-left:28px}

  .card{left:24px;width:108px;height:62px;padding:7px}
  .card .brand{font-size:8px}
  .card .brand-square{width:6px;height:6px}
  .card-name{font-size:5.5px;font-weight:600;margin-top:9px;color:var(--navy)}
  .card-lines{font-size:4px;line-height:1.4;margin-top:2px;white-space:nowrap}
  .card-front{top:139px}
  .card-back{top:235px}
  .card-back .brand,.card-back .card-name{color:var(--realty-brown)}
  .card-back .brand-square{background:var(--realty-brown)}

  .letterhead{top:24px;width:226px;height:295px;padding:12px}
  .letterhead .brand{font-size:10px}
  .letterhead .brand-square{width:8px;height:8px}
  .lh-contact{position:absolute;right:14px;top:12px;font-size:4px;line-height:1.45;text-align:left;white-space:nowrap}
  .lh-band{position:absolute;left:0;right:0;bottom:0;height:12px;background:var(--wealth-blue);color:#fff;font-size:4px;text-align:center;line-height:12px}
  .lh-wealth{left:163px}
  .lh-realty{left:401px}

  .envelope{left:641px;width:182px;height:86px;padding:8px}
  .envelope .brand{font-size:7px}
  .envelope .brand-square{width:6px;height:6px}
  .env-return{font-size:3.6px;line-height:1.4;margin-top:3px}
  .env-band{position:absolute;left:0;right:0;bottom:0;height:6px;background:var(--wealth-blue)}
  .env-one{top:134px}
  .env-two{top:246px}

  .env-back{left:833px;width:338px;height:68px;overflow:hidden}
  .env-back svg{display:block}
  .env-back .seal{position:absolute;left:163px;top:26px;width:12px;height:12px;background:var(--paper)}
  .back-blue{top:36px}
  .back-brown{top:128px}
  .back-white{top:218px}
  .back-white .seal{background:var(--navy)}
</style>
</head>
<body>
<main class="canvas">

  <section class="showcase-brand">
    <div class="brand"><span class="brand-square"></span>BRIGHT HARBOR</div>
    <p class="showcase-sub">Stationery Concepts</p>
  </section>

  <article class="piece card card-front">
    <div class="brand"><span class="brand-square"></span>BRIGHT HARBOR</div>
    <p class="card-name">Dana Verick</p>
    <p class="card-lines">4417 Wexmoor Lane Bozeman, MT 59263<br>406-739-4802<br>dana@brightharborfunds.example<br>www.brightharborfunds.example</p>
  </article>
  <p class="label" style="left:24px;top:205px;width:108px">Front Side</p>

  <article class="piece card card-back">
    <div class="brand"><span class="brand-square"></span>BRIGHT HARBOR</div>
    <p class="card-name">Dana Verick</p>
    <p class="card-lines">4417 Wexmoor Lane Bozeman, MT 59263<br>406-739-4802<br>dana@brightharborestates.example<br>www.brightharborestates.example</p>
  </article>
  <p class="label" style="left:24px;top:302px;width:108px">Back Side</p>

  <article class="piece letterhead lh-wealth">
    <div class="brand"><span class="brand-square"></span>BRIGHT HARBOR</div>
    <p class="lh-contact">4417 Wexmoor Lane<br>Bozeman, MT 59263<br>406-739-4802<br>dana@brightharborfunds.example</p>
    <p class="lh-band">www.brightharborfunds.example</p>
  </article>
  <p class="label" style="left:163px;top:324px;width:226px">Wealth Letterhead</p>

  <article class="piece letterhead lh-realty">
    <div class="brand"><span class="brand-square"></span>BRIGHT HARBOR</div>
    <p class="lh-contact">4417 Wexmoor Lane<br>Bozeman, MT 59263<br>406-739-4802<br>dana@brightharborestates.example</p>
    <p class="lh-band">www.brightharborestates.example</p>
  </article>
  <p class="label" style="left:401px;top:324px;width:226px">Realty Letterhead</p>

  <article class="piece envelope env-one">
    <div class="brand"><span class="brand-square"></span>BRIGHT HARBOR</div>
    <p class="env-return">4417 Wexmoor Lane<br>Bozeman, MT 59263</p>
    <span class="env-band"></span>
  </article>
  <p class="label" style="left:641px;top:225px;width:182px">Envelope Front</p>

  <article class="piece envelope env-two">
    <div class="brand"><span class="brand-square"></span>BRIGHT HARBOR</div>
    <p class="env-return">4417 Wexmoor Lane<br>Bozeman, MT 59263</p>
    <span class="env-band"></span>
  </article>
  <p class="label" style="left:641px;top:335px;width:182px">Envelope Front</p>

  <article class="piece env-back back-blue">
    <svg width="338" height="68" viewBox="0 0 338 68" aria-hidden="true">
      <path d="M0 0H338V14L169 40L0 14Z" fill="var(--wealth-blue)"/>
    </svg>
    <span class="seal"></span>
  </article>
  <article class="piece env-back back-brown">
    <svg width="338" height="68" viewBox="0 0 338 68" aria-hidden="true">
      <path d="M0 0H338V14L169 40L0 14Z" fill="var(--realty-brown)"/>
    </svg>
    <span class="seal"></span>
  </article>
  <article class="piece env-back back-white">
    <svg width="338" height="68" viewBox="0 0 338 68" aria-hidden="true">
      <path d="M0 14L169 40L338 14" fill="none" stroke="var(--paper-edge)" stroke-width="1"/>
    </svg>
    <span class="seal"></span>
  </article>

</main>
</body>
</html>
```